Local Healthy meal delivery service needs a new flyer

Looking for a fresh and modern flyer design for a company called "Brindlecove Fare Works". We provide healthy and delicious meals to families, business offices and health care workers. We would like to see designs that communicate freshness, convenience, non contact delivery and customizable meal plan options. We would like to see designs that mirror our website colors, look and feel: brindlecovefareworks.com

Target Market(s)

Families, Business Offices, Health care workers

Requirements
Must have
• Color scheme and layout matching our brand and website
Our Logo
Modern clean/professional look
contact info: website, phone number, social media
Appropriate photos
Nice to have
• "How it Works" Summary

```html
<!DOCTYPE html>
<html lang="en">
<head>
<meta charset="utf-8">
<title>Brindlecove Fare Works — How It Works</title>
<link href="https://fonts.googleapis.com/css2?family=Oswald:wght@400;500;600&family=Montserrat:wght@400;500;600&display=swap" rel="stylesheet">
<style>
  :root {
    --green: #1e8b4a;
    --green-dark: #176f3a;
    --ink: #2b2b2b;
    --band: rgba(38, 38, 38, 0.78);
    --paper: #ffffff;
    --rule: #b9b9b9;
  }
  * { box-sizing: border-box; margin: 0; padding: 0; }
  html, body { width: 849px; height: 1200px; overflow: hidden; background: var(--paper); }
  .flyer { position: relative; width: 849px; height: 1200px; font-family: "Montserrat", sans-serif; color: var(--ink); }

  .hero {
    position: absolute; left: 0; top: 0; width: 849px; height: 468px;
    background: linear-gradient(135deg, #f3efe8 0%, #e7ddcf 30%, #c9d9b4 55%, #e9a366 75%, #f2ece4 100%);
  }
  .brand-badge {
    position: absolute; left: 50%; top: 0; transform: translateX(-50%);
    width: 220px; height: 232px; background: var(--paper);
    display: flex; flex-direction: column; align-items: center; justify-content: center;
    box-shadow: 0 2px 8px rgba(0,0,0,.15);
  }
  .brand-mark { width: 34px; height: 34px; border-radius: 50%; background: var(--green); margin-bottom: 14px; }
  .brand-name {
    font-family: "Oswald", sans-serif; font-weight: 600; color: var(--green);
    font-size: 30px; line-height: 1.1; text-align: center; text-transform: uppercase; letter-spacing: 1px;
  }
  .hero-band {
    position: absolute; left: 0; top: 258px; width: 849px; height: 190px; background: var(--band);
    color: #fff; text-align: center;
  }
  .headline {
    font-family: "Oswald", sans-serif; font-weight: 500; font-size: 40px; line-height: 1.22;
    letter-spacing: 1px; text-transform: uppercase; margin-top: 30px;
  }
  .contact-row {
    display: flex; justify-content: center; gap: 44px; margin-top: 22px; font-size: 17px;
  }
  .contact-item { display: flex; align-items: center; gap: 9px; }
  .contact-item svg { width: 18px; height: 18px; fill: #fff; }

  .how { position: absolute; top: 500px; left: 0; width: 849px; text-align: center; }
  .how-title { font-family: "Oswald", sans-serif; font-weight: 400; font-size: 52px; letter-spacing: 2px; }
  .how-sub { font-size: 14px; letter-spacing: 2px; margin-top: 4px; }
  .star-rule { display: flex; align-items: center; justify-content: center; gap: 14px; margin-top: 14px; }
  .star-rule span { width: 200px; height: 1px; background: var(--rule); }
  .star-rule svg { width: 22px; height: 22px; fill: #555; }

  .steps { position: absolute; top: 664px; left: 42px; width: 765px; display: flex; justify-content: space-between; }
  .step {
    position: relative; width: 241px; height: 202px; background: var(--green);
    color: #fff; display: flex; align-items: center; justify-content: center; text-align: center;
    padding: 52px 18px 10px;
    font-family: "Oswald", sans-serif; font-weight: 500; font-size: 22px; line-height: 1.3; text-transform: uppercase;
  }
  .step-num {
    position: absolute; top: -34px; left: 50%; transform: translateX(-50%);
    width: 72px; height: 72px; border-radius: 50%; background: var(--green);
    border: 3px solid #fff; outline: 2px solid var(--green);
    display: flex; align-items: center; justify-content: center; font-size: 40px; font-weight: 400;
  }

  .notes { position: absolute; top: 905px; left: 90px; width: 669px; text-align: center; font-size: 15px; line-height: 1.6; }
  .notes .deadline { font-weight: 600; margin-top: 22px; }

  .order-cta { position: absolute; top: 1078px; left: 120px; width: 609px; text-align: center; }
  .order-cta hr { border: 0; height: 1px; background: var(--rule); }
  .order-cta p {
    font-family: "Oswald", sans-serif; color: var(--green); font-size: 30px; letter-spacing: 4px;
    text-transform: uppercase; padding: 18px 0;
  }
</style>
</head>
<body>
<main class="flyer">
  <header class="hero" role="img" aria-label="Overhead photo of fresh vegetables and a cooked meal bowl with rice and roasted vegetables">
    <div class="brand-badge">
      <div class="brand-mark"></div>
      <div class="brand-name">Brindlecove<br>Fare Works</div>
    </div>
    <div class="hero-band">
      <h1 class="headline">We provide fresh, fully cooked,<br>ready to eat meals</h1>
      <div class="contact-row">
        <span class="contact-item">
          <svg viewBox="0 0 24 24"><path d="M6.6 10.8a15 15 0 0 0 6.6 6.6l2.2-2.2a1 1 0 0 1 1-.25 11.4 11.4 0 0 0 3.6.57 1 1 0 0 1 1 1V20a1 1 0 0 1-1 1A17 17 0 0 1 3 4a1 1 0 0 1 1-1h3.5a1 1 0 0 1 1 1c0 1.25.2 2.45.57 3.6a1 1 0 0 1-.25 1z"/></svg>
          555 014 2368
        </span>
        <span class="contact-item">
          <svg viewBox="0 0 24 24"><path d="M12 2a10 10 0 1 0 0 20 10 10 0 0 0 0-20zm6.9 6h-2.9a15.7 15.7 0 0 0-1.4-3.6A8 8 0 0 1 18.9 8zM12 4c.8 1.2 1.5 2.5 1.9 4h-3.8c.4-1.5 1.1-2.8 1.9-4zM4.3 14a8 8 0 0 1 0-4h3.4a16.5 16.5 0 0 0 0 4zm.8 2h2.9c.3 1.3.8 2.5 1.4 3.6A8 8 0 0 1 5.1 16zM8 8H5.1a8 8 0 0 1 4.3-3.6C8.8 5.5 8.3 6.7 8 8zm4 12c-.8-1.2-1.5-2.5-1.9-4h3.8c-.4 1.5-1.1 2.8-1.9 4zm2.3-6H9.7a14.7 14.7 0 0 1 0-4h4.6a14.7 14.7 0 0 1 0 4zm.3 5.6c.6-1.1 1.1-2.3 1.4-3.6h2.9a8 8 0 0 1-4.3 3.6zm1.7-5.6a16.5 16.5 0 0 0 0-4h3.4a8 8 0 0 1 0 4z"/></svg>
          www.brindlecovefareworks.com
        </span>
        <span class="contact-item">
          <svg viewBox="0 0 24 24"><circle cx="12" cy="12" r="9"/></svg>
          @brindlecovefareworks
        </span>
      </div>
    </div>
  </header>

  <section class="how">
    <h2 class="how-title">HOW IT WORKS</h2>
    <p class="how-sub">IN THREE SIMPLE STEPS</p>
    <div class="star-rule">
      <span></span>
      <svg viewBox="0 0 24 24"><path d="M12 2l2.9 6.9 7.1.6-5.4 4.7 1.6 7-6.2-3.8-6.2 3.8 1.6-7L2 9.5l7.1-.6z"/></svg>
      <span></span>
    </div>
  </section>

  <ol class="steps">
    <li class="step"><span class="step-num">1</span>Select the meal plan that works for you</li>
    <li class="step"><span class="step-num">2</span>Choose your delivery day(s)</li>
    <li class="step"><span class="step-num">3</span>Choose regular or portion plus</li>
  </ol>

  <section class="notes">
    <p>MENUS ARE POSTED ON TUESDAY FOR THE FOLLOWING WEEK.</p>
    <p class="deadline">PLEASE PLACE YOUR ORDER BY MIDNIGHT ON SATURDAY FOR THAT WEEK'S DELIVERIES, ANY ORDERS RECEIVED AFTER THAT WILL GO ON THE FOLLOWING WEEKS ORDER.</p>
  </section>

  <footer class="order-cta">
    <hr>
    <p>Place your order online</p>
    <hr>
  </footer>
</main>
</body>
</html>
```